Buch-/E-Book-Cover für einen historischen Roman
Zielgruppe
Buchautor historische Romane, Zielgruppe 60 % weiblich, 35 +
Aufgabenstellung
Die Farbgebung und Schrifttype sollen sich an die ersten 4 Bänder der Serie 'Die Fährmannstochter und der Abt' https://www.buchwelt-beispiel.de/Faehrmannstochter-Abt-Historischer-Roman-ebook/dp/Q471K2XRMZ, anpassen, da der Buchtitel 'Die Gräfin und der Gaukler' der 5 Band dieser Serie ist. Die Grafik kann aber etwas abweichen, im Mittelpunkt des Romans steht das Verschwinden eines Siegelrings. Der sollte abgebildet sein, in dem Roman werden Frau und kleiner Sohn des Herzogs entführt und in einem alten Herrenhaus im englischen Marschland wiedergefunden.

```html
<!DOCTYPE html>
<html lang="de">
<head>
<meta charset="utf-8">
<title>Die Gräfin und der Gaukler – Buch fünf</title>
<link rel="stylesheet" href="https://fonts.googleapis.com/css2?family=Cinzel:wght@400;700&family=IM+Fell+English:ital@1&display=swap">
<style>
  :root {
    --parchment-light: #f1e3bd;
    --parchment-mid: #e6cf98;
    --parchment-edge: #c9a867;
    --author-red: #9c2f35;
    --ink: #141210;
    --ring-light: #cdbb8e;
    --ring-dark: #4a3c22;
    --scene-top: #8a7c72;
    --scene-bottom: #c8bfb0;
    --ground: #4d4a2e;
  }
  html, body {
    margin: 0;
    padding: 0;
    width: 841px;
    height: 1200px;
    overflow: hidden;
    background: var(--parchment-mid);
  }
  .cover {
    position: relative;
    width: 841px;
    height: 1200px;
    overflow: hidden;
    background: radial-gradient(ellipse at 50% 45%, var(--parchment-light) 0%, var(--parchment-mid) 60%, var(--parchment-edge) 100%);
  }
  .author {
    position: absolute;
    top: 50px;
    left: 0;
    width: 100%;
    margin: 0;
    text-align: center;
    font-family: "Cinzel", serif;
    font-weight: 400;
    font-size: 68px;
    line-height: 1;
    color: var(--author-red);
    white-space: nowrap;
  }
  .signet-ring {
    position: absolute;
    top: 210px;
    left: 350px;
    width: 150px;
    height: 90px;
    border-radius: 18px;
    background: radial-gradient(ellipse at 50% 50%, var(--ring-dark) 0%, #7a6840 55%, var(--ring-light) 100%);
  }
  .title {
    position: absolute;
    top: 372px;
    left: 0;
    width: 100%;
    margin: 0;
    text-align: center;
    color: var(--ink);
    font-weight: 400;
  }
  .title .article {
    display: block;
    font-family: "IM Fell English", serif;
    font-style: italic;
    font-size: 66px;
    line-height: 1;
    height: 70px;
  }
  .title .name {
    display: block;
    font-family: "Cinzel", serif;
    font-size: 104px;
    line-height: 1;
    letter-spacing: 1px;
  }
  .title .joiner {
    display: block;
    font-family: "IM Fell English", serif;
    font-style: italic;
    font-size: 58px;
    line-height: 1;
    margin: 16px 0 14px;
  }
  .flourish {
    position: absolute;
    top: 780px;
    left: 354px;
    width: 134px;
    height: 48px;
    border-radius: 50%;
    background: radial-gradient(ellipse, rgba(30,25,20,0.35) 0%, rgba(30,25,20,0) 70%);
  }
  .volume {
    position: absolute;
    top: 877px;
    left: 0;
    width: 100%;
    margin: 0;
    text-align: center;
    font-family: "Cinzel", serif;
    font-weight: 700;
    font-size: 36px;
    line-height: 1;
    color: var(--ink);
  }
  .manor-house {
    position: absolute;
    top: 970px;
    left: 234px;
    width: 381px;
    height: 214px;
    background: linear-gradient(to bottom, var(--scene-top) 0%, var(--scene-bottom) 100%);
  }
  .ground {
    position: absolute;
    bottom: 0;
    left: 0;
    width: 100%;
    height: 16px;
    background: var(--ground);
  }
</style>
</head>
<body>
  <main class="cover">
    <p class="author">TOBIAS KRENNWALD</p>
    <div class="signet-ring" role="img" aria-label="Abbildung eines alten Siegelrings mit verschlungenem Wappen"></div>
    <h1 class="title">
      <span class="article">Die</span>
      <span class="name">GRÄFIN</span>
      <span class="joiner">und der</span>
      <span class="name">GAUKLER</span>
    </h1>
    <div class="flourish" role="img" aria-label="Geschwungenes Schmuckornament"></div>
    <p class="volume">BUCH FÜNF</p>
    <div class="manor-house" role="img" aria-label="Illustration eines alten Herrenhauses mit Ecktürmen im Marschland"></div>
    <div class="ground"></div>
  </main>
</body>
</html>
```